Business Card Design Project

I am a psychotherapist, counselor and expressive arts therapist (means I use every art form imaginable in the service of healing). I'm just starting out in private practice in San Francisco, CA. I work with individual adults, children and families. I'd like the card to mirror the simplicity and color palate of my website. I also would love if there is a symbol, image of fire, flame or spark (that is warming, not frightening).

Check out my website: www.lorabecketmft.com

I want the cards to be printed in letter press so please keep that in mind!

Target Market(s)

Upper Middle Class Adults who are progressively minded, artistic or artists, open to psychotherapy, interested in health & healing.

Industry/Entity Type

Business

Requirements
Must have
• Text to be included:

Lora Becket
Counseling, Psychotherapy & Expressive Arts

2914 Alderwood Avenue, Suite D
San Francisco, CA 94127
p. 415.206.3791
lorajanebecket@meadowpost.net

www.lorabecketmft.com

MFT License Number 48671

It's OK to abbreviate Number to # or Street to St., etc.

Must be compatible with letter press printing.
Nice to have
• I don't have a logo. I don't expect designers to necessarily create one for me, but if someone comes up with a simple image (see above about flame), that would be great. I don't have much of a budget now, but expect that to change in the next year or so and then could buy a logo for my website, future letterhead, etc.

```html
<!DOCTYPE html>
<html lang="en">
<head>
<meta charset="utf-8">
<title>Lora Becket — Business Card</title>
<link href="https://fonts.googleapis.com/css2?family=Libre+Baskerville:wght@400;700&family=Questrial&display=swap" rel="stylesheet">
<style>
  :root {
    --backdrop: #2a2a2b;
    --card: #f2f2f0;
    --ink: #4a4445;
    --accent: #c0283f;
    --accent-soft: #d4475c;
    --decor: #c9c7c6;
  }
  * { margin: 0; padding: 0; box-sizing: border-box; }
  html, body { width: 1200px; height: 900px; overflow: hidden; }
  body {
    background: var(--backdrop);
    position: relative;
    font-family: "Questrial", sans-serif;
    color: var(--ink);
  }
  .card {
    position: absolute;
    left: 285px;
    width: 630px;
    height: 360px;
    background: var(--card);
    border-radius: 18px;
    overflow: hidden;
  }
  .card--front { top: 70px; }
  .card--back { top: 470px; }

  /* Front */
  .front-mark {
    position: absolute;
    left: 50%;
    top: 62px;
    width: 96px;
    height: 96px;
    margin-left: -48px;
    border-radius: 50%;
    background: var(--accent);
  }
  .front-name {
    position: absolute;
    left: 0; right: 0;
    top: 186px;
    text-align: center;
    font-family: "Libre Baskerville", serif;
    font-weight: 700;
    font-size: 50px;
    letter-spacing: 1px;
    color: var(--ink);
  }
  .front-tagline {
    position: absolute;
    left: 0; right: 0;
    top: 258px;
    text-align: center;
    font-family: "Libre Baskerville", serif;
    font-size: 15px;
    color: var(--accent);
  }

  /* Back */
  .back-decor {
    position: absolute;
    right: -110px;
    top: 40px;
    width: 300px;
    height: 300px;
    border-radius: 50%;
    background: var(--decor);
  }
  .back-mark {
    position: absolute;
    left: 52px;
    top: 70px;
    width: 88px;
    height: 88px;
    border-radius: 50%;
    background: var(--accent);
  }
  .back-heading {
    position: absolute;
    left: 180px;
    top: 34px;
    width: 310px;
    text-align: center;
  }
  .back-name {
    font-family: "Libre Baskerville", serif;
    font-weight: 700;
    font-size: 27px;
    color: var(--ink);
  }
  .back-tagline {
    margin-top: 8px;
    font-family: "Libre Baskerville", serif;
    font-size: 12.5px;
    color: var(--accent);
  }
  .back-license {
    margin-top: 6px;
    font-family: "Libre Baskerville", serif;
    font-size: 12.5px;
    color: var(--accent);
  }
  .back-address {
    position: absolute;
    left: 40px;
    top: 196px;
    font-size: 16px;
    line-height: 24px;
  }
  .contact-list {
    position: absolute;
    left: 40px;
    top: 262px;
    list-style: none;
    font-size: 16px;
  }
  .contact-item {
    display: flex;
    align-items: center;
    height: 28px;
  }
  .contact-icon {
    width: 16px;
    height: 16px;
    margin-right: 14px;
    fill: var(--ink);
  }
  .contact-icon--at {
    font-size: 17px;
    width: 16px;
    margin-right: 14px;
    text-align: center;
  }
</style>
</head>
<body>

  <section class="card card--front" aria-label="Card front">
    <div class="front-mark"></div>
    <h1 class="front-name">Lorabecket</h1>
    <p class="front-tagline">Counseling, Psychotherapy &amp; Expressive Arts</p>
  </section>

  <section class="card card--back" aria-label="Card back">
    <div class="back-decor"></div>
    <div class="back-mark"></div>

    <div class="back-heading">
      <h2 class="back-name">Lora Becket</h2>
      <p class="back-tagline">Counseling, Psychotherapy &amp; Expressive Arts</p>
      <p class="back-license">MFT License # 48671</p>
    </div>

    <address class="back-address" style="font-style:normal">
      2914 Alderwood Ave, Suite D<br>
      San Francisco, CA 94127
    </address>

    <ul class="contact-list">
      <li class="contact-item">
        <svg class="contact-icon" viewBox="0 0 24 24" aria-hidden="true">
          <path d="M6.6 10.8a15.1 15.1 0 0 0 6.6 6.6l2.2-2.2a1 1 0 0 1 1-.25 11.4 11.4 0 0 0 3.6.57 1 1 0 0 1 1 1V20a1 1 0 0 1-1 1A17 17 0 0 1 3 4a1 1 0 0 1 1-1h3.5a1 1 0 0 1 1 1c0 1.25.2 2.45.57 3.57a1 1 0 0 1-.25 1z"/>
        </svg>
        <span>415.206.3791</span>
      </li>
      <li class="contact-item">
        <span class="contact-icon--at" aria-hidden="true">@</span>
        <span>lorajanebecket@meadowpost.net</span>
      </li>
      <li class="contact-item">
        <svg class="contact-icon" viewBox="0 0 24 24" aria-hidden="true">
          <path d="M12 3 2 12h3v8h5v-5h4v5h5v-8h3z"/>
        </svg>
        <span>www.lorabecketmft.com</span>
      </li>
    </ul>
  </section>

</body>
</html>
```